Album Jacket for young indie musicians in AFRICA #2 Baraka, Tumaini And Neema (Grace, Hope And Blessing)

We are ZEV SOUND (zev-sound.example), a music label for young African musicians living in a slum. I would like to ask you to design our new album's cover jacket. The title is Baraka, Tumaini And Neema (it means "Grace, Hope And Blessing" in Swahili. I entrust you whether you use English words in the design or not.), musician name is Jabari Okoth. Add our label logo (we have various versions and can provide). I attached Jabari Okoth's photo also. Please listen to the music of the album on Soundcloud. https://tunecove.example/tags/jabariokoth

Target Market(s)

International. not only African music funs.

Requirements
Must have
• Title, Musician's name, ZEV SOUND Logo
• In order to upload to iTunes, I require the final that the following conditions are met.
• 1400 x 1400 pixels
• JPG file type
• 72 - 300dpi (300dpi is the best)
• Less than 25mb
• RGB color scheme (not CMYK)
Nice to have
• His music is something bright and little funny. Please express the tone of music in the design.
Should not have
• African traditional image

```html
<!DOCTYPE html>
<html lang="en">
<head>
<meta charset="utf-8">
<title>Baraka, Tumaini And Neema – Jabari Okoth</title>
<link rel="stylesheet" href="https://fonts.googleapis.com/css2?family=Righteous&display=swap">
<style>
  :root {
    --space-deep: #0c1f0c;
    --space-green: #3f6a1c;
    --space-glow: #e8c21a;
    --space-light: #fbeb8a;
    --star: #fff6b0;
    --gold: #f3c21b;
    --gold-light: #ffe680;
    --gold-dark: #4a2e04;
    --portrait-warm: #e2381e;
    --portrait-deep: #a3180f;
    --portrait-top: #9a5bd0;
    --logo-ink: #111111;
  }
  html, body {
    margin: 0;
    padding: 0;
    overflow: hidden;
    background: #000;
  }
  .album-cover {
    position: relative;
    width: 1200px;
    height: 1200px;
    overflow: hidden;
    font-family: "Righteous", sans-serif;
  }
  .cosmic-backdrop {
    position: absolute;
    inset: 0;
    background:
      radial-gradient(ellipse 50% 38% at 72% 6%, var(--space-light) 0%, rgba(232,194,26,0.75) 30%, rgba(232,194,26,0) 70%),
      radial-gradient(ellipse 40% 30% at 22% 24%, rgba(120,170,40,0.85) 0%, rgba(120,170,40,0) 70%),
      radial-gradient(ellipse 40% 35% at 70% 70%, rgba(170,160,30,0.45) 0%, rgba(170,160,30,0) 70%),
      radial-gradient(ellipse 40% 30% at 8% 55%, rgba(80,140,40,0.5) 0%, rgba(80,140,40,0) 70%),
      linear-gradient(180deg, var(--space-green) 0%, #1f3c14 50%, var(--space-deep) 100%);
  }
  .starfield {
    position: absolute;
    inset: 0;
    width: 1200px;
    height: 1200px;
  }
  .starfield circle { fill: var(--star); }
  .starfield .glow-rays path { fill: var(--space-light); opacity: 0.12; }
  .label-mark {
    position: absolute;
    top: 30px;
    right: 38px;
    display: flex;
    align-items: center;
    gap: 10px;
    font-size: 32px;
    color: var(--logo-ink);
    letter-spacing: 1px;
  }
  .label-mark__dot {
    width: 22px;
    height: 22px;
    border-radius: 50%;
    background: var(--logo-ink);
  }
  .album-title {
    position: absolute;
    top: 88px;
    left: 0;
    width: 1224px;
    margin: 0;
    text-align: center;
    font-weight: 400;
    font-size: 96px;
    line-height: 136px;
    letter-spacing: 5px;
    text-transform: uppercase;
    color: var(--gold);
    -webkit-text-stroke: 3px var(--gold-dark);
    paint-order: stroke fill;
    text-shadow: 0 0 16px rgba(0,0,0,0.6), 0 0 4px var(--gold-light);
  }
  .artist-name {
    position: absolute;
    top: 515px;
    left: 684px;
    margin: 0;
    font-weight: 400;
    font-size: 60px;
    letter-spacing: 1px;
    text-transform: uppercase;
    white-space: nowrap;
    color: var(--gold);
    -webkit-text-stroke: 2px var(--gold-dark);
    paint-order: stroke fill;
    text-shadow: 0 3px 8px rgba(0,0,0,0.6);
  }
  .artist-portrait {
    position: absolute;
    left: 0;
    top: 0;
    width: 1200px;
    height: 1200px;
  }
</style>
</head>
<body>
  <main class="album-cover">
    <div class="cosmic-backdrop"></div>

    <svg class="starfield" viewBox="0 0 1200 1200" role="img" aria-label="Glowing green and golden starfield with light rays">
      <g class="glow-rays">
        <path d="M860 60 L1200 0 L1200 90 Z"/>
        <path d="M860 60 L1200 240 L1200 330 Z"/>
        <path d="M860 60 L700 0 L760 0 Z"/>
        <path d="M860 640 L700 1200 L780 1200 Z"/>
        <path d="M860 640 L1000 1200 L1080 1200 Z"/>
      </g>
      <g class="stars">
        <circle cx="60" cy="90" r="3"/><circle cx="140" cy="40" r="2"/><circle cx="230" cy="120" r="3"/>
        <circle cx="90" cy="260" r="2.5"/><circle cx="40" cy="380" r="3"/><circle cx="160" cy="330" r="2"/>
        <circle cx="250" cy="420" r="2.5"/><circle cx="70" cy="520" r="2"/><circle cx="130" cy="610" r="3"/>
        <circle cx="40" cy="720" r="2.5"/><circle cx="110" cy="820" r="2"/><circle cx="60" cy="930" r="3"/>
        <circle cx="140" cy="1050" r="2"/><circle cx="30" cy="1140" r="2.5"/><circle cx="380" cy="40" r="2"/>
        <circle cx="520" cy="70" r="3"/><circle cx="640" cy="30" r="2.5"/><circle cx="420" cy="330" r="2"/>
        <circle cx="610" cy="360" r="3"/><circle cx="700" cy="400" r="2.5"/><circle cx="780" cy="350" r="3"/>
        <circle cx="880" cy="420" r="2"/><circle cx="960" cy="380" r="3"/><circle cx="1060" cy="330" r="2.5"/>
        <circle cx="1150" cy="400" r="2"/><circle cx="1100" cy="480" r="3"/><circle cx="1010" cy="640" r="2.5"/>
        <circle cx="1140" cy="660" r="3"/><circle cx="960" cy="720" r="2"/><circle cx="1080" cy="780" r="2.5"/>
        <circle cx="1170" cy="860" r="3"/><circle cx="990" cy="900" r="2"/><circle cx="1100" cy="980" r="2.5"/>
        <circle cx="1010" cy="1080" r="3"/><circle cx="1150" cy="1150" r="2"/><circle cx="700" cy="640" r="2.5"/>
        <circle cx="800" cy="680" r="3"/><circle cx="740" cy="740" r="2"/><circle cx="1050" cy="170" r="2.5"/>
        <circle cx="1150" cy="120" r="3"/><circle cx="960" cy="220" r="2"/><circle cx="300" cy="250" r="2.5"/>
        <circle cx="180" cy="460" r="3"/><circle cx="90" cy="1000" r="2"/><circle cx="200" cy="720" r="2.5"/>
      </g>
    </svg>

    <div class="label-mark">
      <span class="label-mark__dot"></span>
      <span class="label-mark__name">ZEV SOUND</span>
    </div>

    <h1 class="album-title">Baraka, Tumaini<br>And Neema</h1>

    <svg class="artist-portrait" viewBox="0 0 1200 1200" role="img" aria-label="Photo of smiling musician Jabari Okoth in a red patterned shirt">
      <defs>
        <linearGradient id="portrait-fill" x1="0" y1="0" x2="0" y2="1">
          <stop offset="0" stop-color="var(--portrait-top)"/>
          <stop offset="0.25" stop-color="var(--portrait-warm)"/>
          <stop offset="1" stop-color="var(--portrait-deep)"/>
        </linearGradient>
      </defs>
      <path fill="url(#portrait-fill)" d="M455 372 C530 372 598 410 600 490 L598 640 C596 690 590 710 600 725 L700 760 C790 790 860 830 900 900 L950 1200 L190 1200 L230 900 C250 820 290 770 380 745 L385 720 C340 690 318 620 316 560 C312 480 330 372 455 372 Z"/>
    </svg>

    <h2 class="artist-name">Jabari Okoth</h2>
  </main>
</body>
</html>
```